Web design project for exciting Australian start-up

Background
We are looking for a creative and talented web design artist to work alongside our market leading web developer.
• You will be required to create a modern and clean design theme for our website, incorporating selected rustic colour scheme elements for our exciting Australian start-up to operate within the coffee industry.
reoccurring work to be expected to flow to the successful designer.
Requirements
• c. 5 - 10 page website
• Landing page
• Log in/ out
• 404 template
• Typography is emphasised
• Please use either a) typevane.com, b) free web fonts, c) marlo fonts
• All design elements in vector format
• Preferably with icons for each header title(i.e. about us, how it works etc) but designer have free reign over how the site looks, so might not be applicable
• All pages to be responsive
• Down to iPad resolution

High level visual design brief attached - additional pages to be worked from base design.

Design inspiration
• We would like to use design elements from the following sources:
http://www.brivantel.com/sorvik/ (Functionality)
Colour scheme refer to logo and complementary style guide
Updates

```html
<!DOCTYPE html>
<html lang="en">
<head>
<meta charset="utf-8">
<title>Brewhaven – Australia's First Online Coffee Marketplace</title>
<link href="https://fonts.googleapis.com/css2?family=Roboto:wght@300;400;500&family=PT+Sans:wght@400;700&display=swap" rel="stylesheet">
<style>
:root{
  --orange:#f7941d;
  --ink:#222;
  --muted:#7a7a7a;
  --rule:#e3e3e3;
  --link-blue:#1ea8dc;
  --footer-bg:#f3f3f3;
  --white:#fff;
}
*{box-sizing:border-box;margin:0;padding:0}
html,body{width:1200px;height:1068px;overflow:hidden;background:var(--white);font-family:"Roboto",sans-serif;color:var(--ink)}
.page{position:relative;width:1200px;height:1068px}
.top-bar{position:absolute;left:0;top:0;width:1200px;height:4px;background:var(--orange)}
.site-header{position:absolute;left:0;top:4px;width:1200px;height:114px}
.brand{position:absolute;left:105px;top:30px;display:flex;align-items:center;gap:10px}
.brand-mark{width:56px;height:56px;border-radius:50%;background:var(--orange)}
.brand-name{font-family:"PT Sans",sans-serif;font-weight:700;font-size:26px;color:var(--ink);letter-spacing:1px}
.auth{position:absolute;left:960px;top:45px;display:flex;border:1px solid var(--ink);height:31px}
.auth a{display:block;width:76px;line-height:29px;text-align:center;font-size:14px;font-weight:300;color:var(--ink);text-decoration:none}
.auth a + a{border-left:1px solid var(--ink);width:86px}
.hero{position:absolute;left:0;top:118px;width:1200px;height:497px;
  background:radial-gradient(ellipse 320px 260px at 370px 200px,#e9e4dd 0%,#c9b9a5 45%,rgba(90,55,30,0) 75%),
  linear-gradient(100deg,#5b3b24 0%,#7a5034 30%,#4a2c18 60%,#3a2212 80%,#8a7a66 100%)}
.hero-shade{position:absolute;inset:0;background:linear-gradient(90deg,rgba(0,0,0,.25),rgba(0,0,0,0) 60%)}
.hero h1{position:absolute;left:103px;font-weight:300;color:var(--white);font-size:64px;line-height:60px;letter-spacing:-.5px}
.hero .h-line1{top:86px}
.hero .accent{position:absolute;left:102px;top:158px;width:481px;height:5px;background:var(--orange)}
.hero .h-line2{top:182px}
.learn-more{position:absolute;left:103px;top:307px;font-size:29px;font-weight:300;color:var(--link-blue);text-decoration:none}
.watch-video{position:absolute;left:104px;top:358px;width:190px;height:49px;border:2px solid var(--white);border-radius:2px;display:flex;align-items:center;gap:11px;padding-left:13px;color:var(--white);font-weight:500;font-size:17px;text-decoration:none}
.info{position:absolute;left:0;top:615px;width:1200px;height:407px}
.col{position:absolute;top:31px;width:200px;text-align:center}
.col-1{left:139px}.col-2{left:480px}.col-3{left:830px}
.col-photo{width:106px;height:106px;border-radius:50%;margin:0 auto}
.photo-a{background:radial-gradient(circle at 50% 40%,#d9d9d9,#555 60%,#1c1c1c)}
.photo-b{background:radial-gradient(circle at 50% 35%,#eee,#888 55%,#222)}
.photo-c{background:radial-gradient(circle at 50% 70%,#fafafa,#bbb 50%,#333)}
.col h2{font-family:"PT Sans",sans-serif;font-weight:700;font-size:22px;margin-top:19px;color:#2a2a2a}
.col ul{list-style:none;width:140px;margin:15px auto 0}
.col li{height:35px;line-height:34px;border-bottom:1px solid var(--rule);font-family:"PT Sans",sans-serif;font-size:15px;color:var(--muted)}
.col li.current::before{content:"";display:inline-block;border:5px solid transparent;border-top:6px solid var(--orange);border-bottom:0;margin-right:10px;vertical-align:2px}
.social li{display:flex;align-items:center;height:39px;line-height:39px;text-align:left}
.social .dot{width:27px;height:27px;border-radius:50%;background:var(--orange);flex:none}
.social .label{flex:1;text-align:center}
.divider{position:absolute;top:90px;width:14px;height:230px;background:radial-gradient(ellipse 7px 115px at 0 50%,rgba(0,0,0,.12),rgba(0,0,0,0))}
.d1{left:407px}.d2{left:758px}
.site-footer{position:absolute;left:0;top:1022px;width:1200px;height:46px;background:var(--footer-bg);border-top:1px solid #dde3e3}
.site-footer p{position:absolute;left:115px;top:15px;font-size:12px;color:#444}
</style>
</head>
<body>
<div class="page">
  <div class="top-bar"></div>
  <header class="site-header">
    <div class="brand"><span class="brand-mark"></span><span class="brand-name">BREWHAVEN</span></div>
    <nav class="auth"><a href="#">Login</a><a href="#">Sign Up</a></nav>
  </header>

  <section class="hero">
    <div role="img" aria-label="Steaming white coffee cup on a wooden table surrounded by roasted coffee beans and a burlap sack" style="position:absolute;inset:0"></div>
    <div class="hero-shade"></div>
    <h1 class="h-line1">Australia’s</h1>
    <div class="accent"></div>
    <h1 class="h-line2">First Online<br>Coffe Marketplace</h1>
    <a class="learn-more" href="#">Learn More</a>
    <a class="watch-video" href="#">
      <svg width="32" height="32" viewBox="0 0 32 32"><circle cx="16" cy="16" r="14.5" fill="none" stroke="#fff" stroke-width="2"/><path d="M13 10l8 6-8 6z" fill="#fff"/></svg>
      WATCH VIDEO
    </a>
  </section>

  <section class="info">
    <div class="col col-1">
      <div class="col-photo photo-a" role="img" aria-label="Black and white photo of a coffee cup on a saucer"></div>
      <h2>Helpful Info</h2>
      <ul>
        <li class="current">About us</li>
        <li>Media Enquiries</li>
        <li>Terms &amp; Conditions</li>
        <li>Privacy Policy</li>
      </ul>
    </div>
    <div class="divider d1"></div>
    <div class="col col-2">
      <div class="col-photo photo-b" role="img" aria-label="Black and white portrait of a smiling man in a suit"></div>
      <h2>Who We Are</h2>
      <ul>
        <li class="current">How It Works</li>
        <li>FAQ</li>
        <li>Contact Us</li>
      </ul>
    </div>
    <div class="divider d2"></div>
    <div class="col col-3">
      <div class="col-photo photo-c" role="img" aria-label="Black and white photo of a cup filled with coffee beans"></div>
      <h2>Join Us On</h2>
      <ul class="social">
        <li><span class="dot"></span><span class="label">Friendloop</span></li>
        <li><span class="dot"></span><span class="label">Chirpline</span></li>
        <li><span class="dot"></span><span class="label">Careernet</span></li>
        <li><span class="dot"></span><span class="label">Viewcast</span></li>
      </ul>
    </div>
  </section>

  <footer class="site-footer"><p>Copyright © 2014 Brewhaven</p></footer>
</div>
</body>
</html>
```